Rio Calmo Lighting Distributors Business Card Design

Use logo and expand the framing box to the extents of the business card. Keep company name in right bottom corner and triangle at top right corner. I would like to have a template so that I can fill in employee name, contact info, email and website.

```html
<!DOCTYPE html>
<html lang="en">
<head>
<meta charset="utf-8">
<title>Rio Calmo Lighting Distributors – Business Card</title>
<link rel="stylesheet" href="https://fonts.googleapis.com/css2?family=Montserrat:wght@400;500;600;800&display=swap">
<style>
  :root {
    --backdrop: #0b82c4;
    --navy: #03202f;
    --ink: #0e1e2a;
    --accent: #0a84c8;
    --paper: #ffffff;
  }
  * { box-sizing: border-box; margin: 0; padding: 0; }
  html, body {
    width: 1200px; height: 1200px; overflow: hidden;
    background: var(--backdrop);
    font-family: "Montserrat", sans-serif;
  }
  .card {
    position: absolute;
    left: 150px;
    width: 900px; height: 514px;
    box-shadow: 0 10px 30px rgba(0, 20, 40, 0.35);
  }
  .card--back { top: 60px; background: var(--navy); }
  .card--front { top: 626px; background: var(--paper); }
  .card-frame { position: absolute; inset: 0; width: 100%; height: 100%; }

  .contact-block {
    position: absolute; left: 80px; top: 352px;
    color: var(--paper);
  }
  .employee-name {
    color: var(--accent); font-weight: 600; font-size: 36px;
    letter-spacing: 1px; line-height: 1;
  }
  .employee-position {
    font-weight: 500; font-size: 17px; letter-spacing: 1.5px; margin-top: 6px;
  }
  .contact-list { list-style: none; margin-top: 14px; }
  .contact-list li {
    display: flex; align-items: center; gap: 14px;
    font-size: 19px; font-weight: 500; line-height: 1; margin-bottom: 9px;
  }
  .contact-icon { width: 22px; height: 22px; flex: none; }

  .company-name {
    position: absolute; left: 80px; top: 338px;
    color: var(--ink); font-weight: 800; font-size: 54px;
    line-height: 0.98; letter-spacing: -1px; text-transform: uppercase;
  }
</style>
</head>
<body>

<section class="card card--back" aria-label="Business card back with employee contact details">
  <svg class="card-frame" viewBox="0 0 900 514" aria-hidden="true">
    <polygon points="425,44 857,44 857,215" fill="var(--accent)"/>
    <g stroke="var(--paper)" stroke-width="14" fill="none" stroke-linecap="butt">
      <polyline points="405,50 50,50 50,340"/>
      <polyline points="850,240 850,464 480,464"/>
    </g>
  </svg>
  <div class="contact-block">
    <h1 class="employee-name">FULL NAME</h1>
    <p class="employee-position">POSITION</p>
    <ul class="contact-list">
      <li>
        <svg class="contact-icon" viewBox="0 0 24 24" aria-hidden="true"><path fill="var(--accent)" d="M6.6 10.8a15.1 15.1 0 0 0 6.6 6.6l2.2-2.2a1 1 0 0 1 1-.25 11.4 11.4 0 0 0 3.6.57 1 1 0 0 1 1 1V20a1 1 0 0 1-1 1A17 17 0 0 1 3 4a1 1 0 0 1 1-1h3.5a1 1 0 0 1 1 1c0 1.25.2 2.45.57 3.57a1 1 0 0 1-.25 1z"/></svg>
        (000) 000 0000
      </li>
      <li>
        <svg class="contact-icon" viewBox="0 0 24 24" aria-hidden="true"><rect x="2" y="5" width="20" height="14" fill="var(--accent)"/><polyline points="2,5 12,13 22,5" fill="none" stroke="var(--navy)" stroke-width="1.6"/></svg>
        email@company.com
      </li>
      <li>
        <svg class="contact-icon" viewBox="0 0 24 24" aria-hidden="true"><g fill="none" stroke="var(--accent)" stroke-width="1.8"><circle cx="12" cy="12" r="10"/><ellipse cx="12" cy="12" rx="4.5" ry="10"/><line x1="2" y1="12" x2="22" y2="12"/><line x1="4" y1="7" x2="20" y2="7"/><line x1="4" y1="17" x2="20" y2="17"/></g></svg>
        www.company.com
      </li>
    </ul>
  </div>
</section>

<section class="card card--front" aria-label="Business card front with company name">
  <svg class="card-frame" viewBox="0 0 900 514" aria-hidden="true">
    <polygon points="425,44 857,44 857,215" fill="var(--accent)"/>
    <g stroke="var(--ink)" stroke-width="14" fill="none" stroke-linecap="butt">
      <polyline points="405,50 50,50 50,320"/>
      <polyline points="850,240 850,464 600,464"/>
    </g>
  </svg>
  <h2 class="company-name">Rio Calmo<br>Lighting<br>Distributors</h2>
</section>

</body>
</html>
```